Post card design for pool service company

This card is for getting pool owners to call us concerning pool service. Post card size is 6"x8" printed. My website is tidewhisk.net for additional information and color schemes. I want the card to compliment our logo colors. I've uploaded a design I like, but I want it to be unique rather than simply copied. Can you improve on the design sample I've included? I included logo and our wrapped truck which I would like incorporated into the post card. The truck pic can be whole or partial, as long as the name and pic is visible. Thanks!

Target Market(s)

Swimming pool owners looking for pool service

Industry/Entity Type

Swimming pool service

Colors
0054AA
0677BA
7BADD7
CADEEF
E8F1F8
EE7325
F08F49
F5BC92
FAE3D3
FDF4ED

Requirements
Must have
• Truck (partial ok, or full picture). Phone number is 619-382-7096. I'd like the card to let the client know they can either call or text. Also include the logo front and back where appropriate.
Nice to have
• A different picture than the one in the example that is uploaded.

```html
<!DOCTYPE html>
<html lang="en">
<head>
<meta charset="utf-8">
<title>Tidewhisk Postcard</title>
<link rel="stylesheet" href="https://fonts.googleapis.com/css2?family=Bebas+Neue&family=Oswald:wght@600;700&family=Merriweather:ital,wght@0,400;0,700;1,400&family=Saira:wght@700&display=swap">
<style>
  :root {
    --navy: #1456a8;
    --sky: #5ea6dc;
    --orange: #e94025;
    --water-deep: #1aa3c9;
    --water-light: #5fd3e6;
    --ink: #111111;
    --white: #ffffff;
    --stamp: #e3e4e8;
    --page: #b1b2b1;
  }
  * { margin: 0; padding: 0; box-sizing: border-box; }
  html, body { width: 800px; height: 1200px; overflow: hidden; }
  body { background: var(--page); position: relative; }

  .card { position: absolute; left: 86px; width: 629px; height: 472px; background: var(--white); overflow: hidden; }
  .card--front { top: 83px; }
  .card--back { top: 622px; }
  .layer { position: absolute; left: 0; top: 0; }

  .headline { position: absolute; left: 27px; top: 36px; font-family: "Bebas Neue", sans-serif; font-weight: 400; line-height: 0.8; color: var(--navy); text-transform: uppercase; }
  .headline__line { display: block; font-size: 86px; }
  .headline__line--accent { color: var(--sky); }
  .headline__line--small { font-size: 53px; margin-top: 3px; }

  .subhead { position: absolute; left: 27px; top: 226px; font-family: "Merriweather", serif; font-weight: 700; font-size: 17px; line-height: 1.25; color: var(--navy); }

  .call-text { position: absolute; left: 27px; top: 294px; font-family: "Merriweather", serif; font-weight: 700; font-size: 21px; line-height: 1.2; color: var(--white); }

  .contact-box { position: absolute; left: 27px; top: 354px; width: 277px; height: 80px; background: var(--orange); border-radius: 9px; text-align: center; color: var(--white); }
  .contact-box__phone { font-family: "Saira", sans-serif; font-weight: 700; font-size: 34px; line-height: 1; padding-top: 8px; }
  .contact-box__rule { width: 238px; height: 1px; background: var(--white); margin: 6px auto 7px; }
  .contact-box__web { font-family: "Oswald", sans-serif; font-weight: 600; font-size: 16px; letter-spacing: 6px; text-transform: uppercase; }

  .brand { position: absolute; font-family: "Oswald", sans-serif; font-weight: 700; text-transform: uppercase; line-height: 1; }
  .brand--front { right: 30px; top: 62px; font-size: 34px; color: var(--navy); display: flex; align-items: center; gap: 7px; }
  .brand__dot { width: 14px; height: 14px; border-radius: 50%; background: var(--orange); }
  .brand--back { right: 30px; top: 382px; font-size: 28px; color: var(--navy); }

  .tag { position: absolute; left: 29px; top: 37px; font-family: "Bebas Neue", sans-serif; font-weight: 400; font-size: 22px; line-height: 0.95; color: var(--white); text-transform: uppercase; }

  .feature { position: absolute; width: 112px; text-align: center; font-family: "Merriweather", serif; font-size: 10.5px; line-height: 1.15; color: var(--ink); }
  .feature__icon { display: block; width: 50px; height: 50px; margin: 0 auto 8px; border-radius: 12px; background: linear-gradient(135deg, #cadeef, #fae3d3); }

  .stamp { position: absolute; left: 511px; top: 18px; width: 99px; height: 99px; background: var(--stamp); border: 1px dashed #b8bac0; }

  .divider-v { position: absolute; left: 315px; top: 94px; width: 4px; height: 311px; background: var(--ink); }
  .divider-h { position: absolute; left: 16px; top: 283px; width: 283px; height: 2px; background: var(--ink); }
  .address-line { position: absolute; left: 355px; width: 245px; height: 2px; background: var(--ink); }

  .offer { position: absolute; left: 29px; top: 305px; font-family: "Bebas Neue", sans-serif; font-weight: 400; font-size: 20px; line-height: 0.95; color: var(--ink); text-transform: uppercase; }
  .price { position: absolute; left: 166px; top: 297px; font-family: "Saira", sans-serif; font-weight: 700; font-size: 44px; line-height: 1; color: var(--orange); }
  .price__sign { font-size: 20px; vertical-align: 18px; }
  .price-note { position: absolute; left: 250px; top: 309px; font-family: "Merriweather", serif; font-style: italic; font-size: 7.5px; color: var(--navy); }

  .truck { position: absolute; left: 31px; top: 362px; width: 240px; height: 84px; border-radius: 16px 22px 10px 10px; background: linear-gradient(180deg, #ee7325 0%, #f08f49 45%, #0677ba 55%, #0054aa 100%); }
</style>
</head>
<body>

<section class="card card--front" aria-label="Postcard front">
  <svg class="layer" width="629" height="472" viewBox="0 0 629 472">
    <defs>
      <linearGradient id="water" x1="0" y1="0" x2="1" y2="1">
        <stop offset="0" stop-color="#5fd3e6"/>
        <stop offset="1" stop-color="#1aa3c9"/>
      </linearGradient>
    </defs>
    <path role="img" aria-label="Aerial photo of two swimmers on inflatable floats in a bright blue pool" d="M134 472 C 300 420, 360 190, 629 102 L629 472 Z" fill="url(#water)"/>
    <path d="M0 281 H362 L391 398 H0 Z" fill="var(--navy)"/>
  </svg>

  <h1 class="headline">
    <span class="headline__line">Keep your</span>
    <span class="headline__line headline__line--accent">Pool blue</span>
    <span class="headline__line headline__line--small">All year round!</span>
  </h1>
  <p class="subhead">Weekly &amp; Bi-weekly swimming<br>pool maintenance &amp; services</p>
  <p class="call-text">CALL OR TEXT US today to<br>schedule your free pool quote!</p>
  <div class="contact-box">
    <div class="contact-box__phone">(619) 382-7096</div>
    <div class="contact-box__rule"></div>
    <div class="contact-box__web">www.tidewhisk.net</div>
  </div>
  <div class="brand brand--front"><span class="brand__dot"></span>Tidewhisk</div>
</section>

<section class="card card--back" aria-label="Postcard back">
  <svg class="layer" width="629" height="472" viewBox="0 0 629 472">
    <path d="M0 0 H514 C 460 18, 440 74, 350 71 C 250 68, 120 72, 0 105 Z" fill="var(--navy)"/>
    <path d="M0 31 H247 L220 83 H0 Z" fill="var(--orange)"/>
    <path d="M0 384 C 80 400, 130 430, 220 438 C 360 446, 480 400, 629 428 V472 H0 Z" fill="var(--orange)"/>
    <path d="M0 398 C 80 420, 150 446, 240 448 C 380 448, 500 415, 629 437 V472 H0 Z" fill="var(--navy)"/>
  </svg>

  <h2 class="tag">Our pool maintenance<br>always includes:</h2>
  <div class="stamp" aria-label="Stamp area"></div>

  <div class="feature" style="left:43px; top:94px;"><span class="feature__icon" role="img" aria-label="Icon of a hand holding a gear with a chemical flask"></span>Full Service<br>Including Chemicals</div>
  <div class="feature" style="left:157px; top:94px;"><span class="feature__icon" role="img" aria-label="Icon of a stopwatch beside a pool technician"></span>Same Day,<br>Same Pool Technician</div>
  <div class="feature" style="left:26px; top:186px;"><span class="feature__icon" role="img" aria-label="Icon of a headset ringed by stars"></span>5-Star<br>Customer Service</div>
  <div class="feature" style="left:103px; top:186px;"><span class="feature__icon" role="img" aria-label="Icon of a paw print with a check mark"></span>Pet Friendly<br>(Woof!)</div>
  <div class="feature" style="left:183px; top:186px;"><span class="feature__icon" role="img" aria-label="Icon of a brush, germs and a protective shield"></span>“No Green Pool”<br>Guarantee</div>

  <div class="divider-h"></div>
  <div class="divider-v"></div>
  <div class="address-line" style="top:254px;"></div>
  <div class="address-line" style="top:283px;"></div>
  <div class="address-line" style="top:312px;"></div>
  <div class="address-line" style="top:341px;"></div>
  <div class="address-line" style="top:370px;"></div>

  <p class="offer">Our most popular<br>plan starts at only</p>
  <p class="price"><span class="price__sign">$</span>125</p>
  <p class="price-note">(Most Pools)</p>

  <div class="truck" role="img" aria-label="Company pickup truck with orange and blue wrap showing the company name and phone number"></div>
  <div class="brand brand--back">Tidewhisk</div>
</section>

</body>
</html>
```